Cabling Business Graphic Design for Website

Hi,

We need a three pages designed for a cabling website: http://www.wiremarta.com.au/

1.) Homepage
2.) Category Page
3.) Product Page

Wiremarta is an online wholesaler of Server Racks and Cables.

Wiremarta began in 2006 as an offshoot of a cabling installation company called Voltrinex which has been around since 1993. Through Voltrinex and the industry insight that gave use we saw the need for a direct, online wholesaler.

The problem we found the with the industry is the middle man. It seemed that industry suppliers were so obsessed with carving out distribution channels and establishing exclusive resellers and wholesalers that they began to alienate their products and price themselves out of the market.

Then came Wiremarta - the first direct online data comms wholesaler to hit the industry.

We manufacture, import and sell direct - we have no middle men, keep our prices fair and our product range fresh.

Top three competitors:
Pivotal Brookware - www.dorvane.com.au
Shelvora - www.shelvora.com.au
Quendel Networks - www.quendel.net.au

Our range - we offer a massive range of products - we are always adding new and unique products.

Our Service - we have technical sales staff who are able to help with technical questions and provide advice on how to do things / what to buy - its not just a call centre situation.

We are able to custom manufacture cables and cabinets to suit specifications.

Its very easy to order from us, our turnaround time is 99% of the time 24 hours.

Please refer to the design brief file and the business uncovery for more information. The design brief files are quite specific so please ensure the design adheres to this brief.

Target Market(s)

IT Managers, Electricians, Network Integrators and IT companies.

They have a contract with schools and government departments to order their supplies. This is a massive section of their market.

Industry/Entity Type

Industry

Requirements
Must have
• Reinforce
* that the products adhere to government and industry certifications
* warranty / quality guarantee
* delivery details / stock availability
Nice to have
• Included in the Business Uncovery file
Should not have
• Included in the Business Uncovery

```html
<!DOCTYPE html>
<html lang="en">
<head>
<meta charset="utf-8">
<title>Wiremarta – Server Racks &amp; Cables Wholesale</title>
<link rel="stylesheet" href="https://fonts.googleapis.com/css2?family=Arimo:wght@400;700&family=Tinos:ital@1&display=swap">
<style>
:root{
  --red:#c8171c;
  --red-dark:#9e0f12;
  --black:#0d0d0d;
  --ink:#333;
  --muted:#666;
  --line:#d6d6d6;
  --panel:#f4f4f4;
  --white:#fff;
  --footer:#141414;
  --footer-bar:#242424;
}
*{box-sizing:border-box;margin:0;padding:0}
html,body{width:874px;height:1200px;overflow:hidden}
body{background:var(--black);font-family:Arimo,Arial,sans-serif;color:var(--ink);position:relative}
.abs{position:absolute}
.top-rule{left:0;top:0;width:874px;height:4px;background:var(--red)}

/* header */
.brand{left:52px;top:38px;display:flex;align-items:center;gap:8px}
.brand-mark{width:20px;height:20px;background:var(--red)}
.brand-name{font-size:32px;font-weight:700;color:var(--white);letter-spacing:-1px}
.search{left:249px;top:50px;width:420px;height:51px;background:#e9e9e9;border-radius:3px;display:flex;align-items:center;padding:0 8px;gap:6px}
.search-field{flex:1;height:28px;background:var(--white);border:1px solid #c9c9c9;border-radius:3px;font-size:10px;color:#888;padding:7px 8px}
.search-btn{width:80px;height:28px;background:var(--red);border-radius:4px;color:var(--white);font-size:13px;font-weight:700;text-align:center;line-height:28px}
.support-figure{left:696px;top:30px;width:26px;height:30px;background:linear-gradient(#b22,#622);border-radius:4px}
.support-text{left:743px;top:34px;font-size:10px;color:#ddd;line-height:14px}
.phone{left:706px;top:73px;display:flex;align-items:center;gap:20px;color:var(--white);font-size:15px}
.hours{left:700px;top:99px;font-size:9px;color:#ddd}

/* page */
.page{left:33px;top:119px;width:810px;height:871px;background:var(--white)}
.nav{left:40px;top:127px;width:797px;height:28px;background:var(--red);display:flex;align-items:center;padding-left:6px;white-space:nowrap}
.nav a{color:var(--white);font-size:10px;font-weight:700;text-decoration:none;padding:0 3.5px;text-transform:uppercase;letter-spacing:-0.2px;white-space:nowrap}
.nav a.account{margin-left:auto;background:var(--red-dark);color:#111;height:28px;line-height:28px;padding:0 10px;font-weight:400}

.sidebar{left:40px;top:164px;width:159px;height:323px;background:var(--panel);border:1px solid var(--line)}
.sidebar li{list-style:none;height:24px;line-height:24px;padding-left:8px;font-size:10px;font-weight:700;border-bottom:1px solid var(--white);position:relative;color:#222;white-space:nowrap}
.sidebar li.chev::after{content:"›";position:absolute;right:8px;top:-1px;color:#1d4f9a;font-size:15px}

.intro-title{left:212px;top:170px;font-size:16px;color:#333;font-weight:400}
.intro-text{left:212px;top:200px;width:455px;font-size:9.6px;line-height:16px;color:var(--muted)}

.tile{width:106px;height:132px;background:var(--red);border:3px solid #ddd}
.tile-label{width:130px;text-align:center;font-size:10px;color:#555;line-height:12px;letter-spacing:.5px}
.tile-wm{display:flex;align-items:center;justify-content:center;color:var(--white);font-size:13px;font-weight:700}

.divider{left:208px;top:529px;width:461px;border-top:1px dotted #999}
.top-selling{left:208px;top:542px;width:461px;height:27px;background:linear-gradient(var(--red),var(--red-dark));color:var(--white);font-size:15px;padding:4px 6px}
.top-selling span{position:absolute;right:10px;top:8px;font-size:9px;font-weight:700}

/* right column */
.side-head{left:675px;width:159px;height:28px;background:linear-gradient(var(--red),var(--red-dark));color:var(--white);font-size:14px;padding:6px 10px;text-transform:uppercase;white-space:nowrap}
.side-head.cert{font-size:13px;letter-spacing:-0.2px;padding:6px 8px;line-height:18px}
.side-box{left:675px;width:159px;background:var(--panel);border:1px solid var(--line)}
.basket{left:690px;top:214px;width:42px;height:34px;background:linear-gradient(#f5c422,#d99a0a);border-radius:3px}
.cart-info{left:748px;top:220px;font-size:10px;color:#444;line-height:18px}
.btn{height:22px;border-radius:4px;font-size:10px;text-align:center;line-height:22px}
.btn-red{background:var(--red);color:var(--white)}
.btn-grey{background:#e2e2e2;color:var(--red)}
.why-figure{left:788px;top:326px;width:40px;height:48px;background:linear-gradient(#888,#333);border-radius:6px 6px 0 0}
.badge{left:710px;top:444px;width:90px;height:76px;background:var(--white);border:1px solid var(--line)}
.badge-shape{left:720px;top:456px;width:70px;height:52px;background:linear-gradient(90deg,#c8171c 50%,#1b3f86 50%);border-radius:4px}
.news-title{left:684px;top:599px;font-size:12px;color:#555;text-transform:uppercase}
.news-text{left:684px;top:616px;width:140px;font-size:9.5px;line-height:14px;color:#888}
.news-field{left:682px;top:663px;width:144px;height:22px;background:var(--white);border:1px solid #ccc;font-size:9px;color:#777;padding:5px 6px}
.news-btn{left:682px;top:696px;width:144px;height:26px;background:#111;color:var(--white);border-radius:4px;font-size:11.5px;font-weight:700;text-align:center;line-height:26px}
.cards{left:688px;top:756px;display:flex;gap:4px}
.cards i{width:28px;height:16px;background:#5a7fb8;border-radius:2px;display:block}
.secure{left:692px;top:784px;display:flex;align-items:center;gap:6px;font-size:10px;font-weight:700;color:var(--red)}
.quote{left:682px;top:861px;width:145px;height:80px;background:#e4e4e4;padding:5px 6px 0 22px;font-family:Tinos,serif;font-style:italic;font-size:10px;line-height:12.5px;color:#555;text-align:right}
.quote-mark{left:686px;top:852px;font-family:Tinos,serif;font-size:46px;color:#c9c9c9}
.quote-name{left:730px;top:946px;font-size:10px;color:#333}
.more-link{left:778px;top:962px;font-size:10px;color:var(--red)}

/* footer */
.foot-links{left:33px;top:990px;width:810px;height:32px;background:var(--footer-bar);display:flex;justify-content:center;align-items:center;font-size:10px;color:#ddd}
.foot-links span{padding:0 8px;border-left:1px solid #555}
.foot-links span:first-child{border:none}
.foot-cols{left:33px;top:1022px;width:810px;height:143px;display:flex;padding:15px 8px 0 8px}
.foot-col{padding:0 8px;border-right:1px solid #333;height:120px}
.foot-col:last-child{border:none}
.foot-col h4{font-size:9px;color:var(--white);font-weight:700;margin-bottom:10px;white-space:nowrap}
.foot-col p{font-size:9.5px;color:#ccc;line-height:16px;white-space:nowrap}
.copyright{left:0;top:1165px;width:874px;height:35px;background:var(--footer);font-size:10px;color:#ccc;text-align:center;line-height:35px}
.social{top:1174px;width:20px;height:20px;border-radius:3px}
</style>
</head>
<body>
<div class="abs top-rule"></div>

<header>
  <div class="abs brand"><span class="brand-mark"></span><span class="brand-name">Wiremarta</span></div>
  <div class="abs search"><div class="search-field">Search Term</div><div class="search-btn">Search</div></div>
  <div class="abs support-figure" role="img" aria-label="Support agent illustration"></div>
  <div class="abs support-text">Need Support?<br>Live Chat</div>
  <div class="abs phone">
    <svg width="14" height="14" viewBox="0 0 24 24"><path fill="#fff" d="M6.6 10.8a15 15 0 0 0 6.6 6.6l2.2-2.2a1 1 0 0 1 1-.25 11.4 11.4 0 0 0 3.6.57 1 1 0 0 1 1 1V20a1 1 0 0 1-1 1A17 17 0 0 1 3 4a1 1 0 0 1 1-1h3.5a1 1 0 0 1 1 1c0 1.25.2 2.45.57 3.6a1 1 0 0 1-.25 1z"/></svg>
    <span>123 456 7890</span>
  </div>
  <div class="abs hours">Mon - Fri ( 9am - 5pm ) AEST</div>
</header>

<main class="abs page"></main>

<nav class="abs nav">
  <a>Home</a><a>About Us</a><a>Our Catalogue</a><a>Wholesale Outlet Stores</a><a>Education / Government</a><a>Shipping</a><a>Payments</a><a>Contact Us</a><a class="account">Account / Login</a>
</nav>

<ul class="abs sidebar">
  <li class="chev">Cables</li><li class="chev">Data Product</li><li class="chev">Server Cabinets</li><li class="chev">Network Cabinets</li><li class="chev">Fiber Products</li><li class="chev">Coax Products</li><li class="chev">Telephone &amp; Voice</li><li class="chev">Tools &amp; Switches</li><li>&amp; Hardware</li><li class="chev">AV Wall Plates &amp; Inserts</li><li class="chev">Plasma &amp; LCD Brackets</li><li class="chev">Cable Ducting Conduit</li>
</ul>

<h1 class="abs intro-title">Lorem ipsum dolor sit amet, consectetuer</h1>
<p class="abs intro-text">Lorem ipsum dolor sit amet, consectetuer adipiscing elit. Aenean commodo ligula eget dolor. Aenean massa. Cum sociis natoque penatibus et magnis dis parturient montes, nascetur ridiculus mus. Donec quam felis, ultricies nec, pellentesque eu, pretium quis, sem. Nulla consequat massa quis enim. Donec pede justo, fringilla vel, aliquet nec, vulputate eget, arcu. In enim justo, rhoncus ut, imperdiet a, venenatis vitaLorem ipsum dolor sit amet, consectetuer adipiscing elit. Aenean commodo ligula eget dolor. Aenean massa. Cum sociis natoque penatibus et magnis dis parturient montes, nascetur ridiculus mus. Donec quam felis, ultricies nec, Aenean massa. Cum sociis natoque penatibus et magnis dis parturient montes, nascetur ridiculus mus.</p>

<div class="abs tile" style="left:208px;top:338px" role="img" aria-label="Cables category image"></div>
<div class="abs tile" style="left:326px;top:338px" role="img" aria-label="Cable management category image"></div>
<div class="abs tile" style="left:444px;top:338px" role="img" aria-label="Data products category image"></div>
<div class="abs tile" style="left:561px;top:338px" role="img" aria-label="Server rack cabinets category image"></div>
<div class="abs tile-label" style="left:196px;top:476px">Cables</div>
<div class="abs tile-label" style="left:314px;top:476px">Cable Management</div>
<div class="abs tile-label" style="left:432px;top:476px">Data Products</div>
<div class="abs tile-label" style="left:549px;top:476px">Server Rack<br>Cabinets</div>

<div class="abs divider"></div>
<div class="abs top-selling">Top Selling Products<span>more</span></div>

<div class="abs tile" style="left:208px;top:585px" role="img" aria-label="Network cable product image"></div>
<div class="abs tile" style="left:326px;top:585px" role="img" aria-label="Network cable product image"></div>
<div class="abs tile" style="left:444px;top:585px" role="img" aria-label="Network cable product image"></div>
<div class="abs tile" style="left:561px;top:585px" role="img" aria-label="Network cable product image"></div>
<div class="abs tile-label" style="left:196px;top:726px">Network Cable</div>
<div class="abs tile-label" style="left:314px;top:726px">Network Cable</div>
<div class="abs tile-label" style="left:432px;top:726px">Network Cable</div>
<div class="abs tile-label" style="left:549px;top:726px">Network Cable</div>

<div class="abs tile" style="left:208px;top:761px" role="img" aria-label="Network cable product image"></div>
<div class="abs tile" style="left:326px;top:761px" role="img" aria-label="Network cable product image"></div>
<div class="abs tile tile-wm" style="left:444px;top:761px">Wiremarta</div>
<div class="abs tile" style="left:561px;top:761px" role="img" aria-label="Network cable product image"></div>
<div class="abs tile-label" style="left:196px;top:906px">Network Cable</div>
<div class="abs tile-label" style="left:314px;top:906px">Network Cable</div>
<div class="abs tile-label" style="left:432px;top:906px">Network Cable</div>
<div class="abs tile-label" style="left:549px;top:906px">Network Cable</div>

<aside>
  <div class="abs side-head" style="top:165px">Shopping Cart</div>
  <div class="abs side-box" style="top:193px;height:125px"></div>
  <div class="abs basket" role="img" aria-label="Shopping basket icon"></div>
  <div class="abs cart-info">Items: 0<br>Total: $0.00</div>
  <div class="abs btn btn-red" style="left:688px;top:284px;width:62px">View cart</div>
  <div class="abs btn btn-grey" style="left:757px;top:284px;width:64px">Checkout</div>

  <div class="abs side-head" style="top:331px;height:42px;padding-top:12px">Why Client?</div>
  <div class="abs why-figure" role="img" aria-label="Customer service person illustration"></div>

  <div class="abs side-head cert" style="top:381px;height:49px">Certificates &amp;<br>Quality Assurance</div>
  <div class="abs side-box" style="top:430px;height:119px"></div>
  <div class="abs badge"></div>
  <div class="abs badge-shape"></div>

  <div class="abs side-head" style="top:565px">Our Newsletter</div>
  <div class="abs side-box" style="top:593px;height:142px"></div>
  <div class="abs news-title">Join our newsletter</div>
  <div class="abs news-text">Discover exclusive offers, products previews and much more......</div>
  <div class="abs news-field">Enter your mail</div>
  <div class="abs news-btn">GET SPECIAL OFFERS</div>

  <div class="abs side-box" style="top:744px;height:70px"></div>
  <div class="abs cards"><i></i><i></i><i></i><i style="width:34px"></i></div>
  <div class="abs secure">
    <svg width="12" height="14" viewBox="0 0 12 14"><rect x="1" y="6" width="10" height="8" rx="1" fill="#c8171c"/><path d="M3 6V4a3 3 0 0 1 6 0v2" stroke="#888" stroke-width="1.5" fill="none"/></svg>
    100% Secure shopping
  </div>

  <div class="abs side-head" style="top:823px">Testimonials</div>
  <div class="abs side-box" style="top:851px;height:126px"></div>
  <div class="abs quote">Lorem ipsum dolor sit amet, consectetuer adipi-scing elit. Aenean commodo ligula eget dolor. Aenean massa. Cum sociis nat.</div>
  <div class="abs quote-mark">“</div>
  <div class="abs quote-name">NAME</div>
  <div class="abs more-link">View more</div>
</aside>

<footer>
  <div class="abs foot-links"><span>Home</span><span>About Wiremarta</span><span>My Account</span><span>Order Status</span><span>Wish List</span><span>Gift Certificate</span><span>View Cart</span><span>Sign In</span><span>Create An Account</span></div>
  <div class="abs foot-cols">
    <div class="foot-col" style="width:245px"><h4>SERVER RACKS / NETWORK COMPUTER CABINETS</h4><p>Network Cabinet &amp; Rack Mount Accesories<br>Wall Mount Network Cabinets<br>Half Height Floor Server Racks<br>Full Height Server Racks<br>Wall Mount Frames<br>Network Cabinet Shelves</p></div>
    <div class="foot-col" style="width:145px"><h4>CABLE MANAGEMENT</h4><p>Cable Management Rings<br>Cable Floor Covers<br>Cable Management Rails<br>Cable Ties<br>Cable Tray</p></div>
    <div class="foot-col" style="width:112px"><h4>ETHERNET CABLES</h4><p>Cat 5E Cable<br>Cat 6 Cable</p></div>
    <div class="foot-col" style="width:183px"><h4>FIBRE PRODUCTS</h4><p>Multimode Fibre Optic Patch Cables<br>Single Mode Fibre Optic Patch Leads<br>Fibre Optic Cable</p></div>
    <div class="foot-col" style="width:110px"><h4>PATCH PANELS</h4><p>Cat5e Patch Panel<br>Cat 6 Patch Panels</p></div>
  </div>
  <div class="abs copyright">Copyright 2011 Wiremarta. All rights reserved. Terms and conditions</div>
  <div class="abs social" style="left:752px;background:#3b5a99"></div>
  <div class="abs social" style="left:778px;background:#3aa5d8"></div>
</footer>
</body>
</html>
```